Web Design Project HopeHaven - Design+Coding

HopeHaven-Temecula needs a new website! Design + Coding required.

This church is looking for a highly designed, highly interactive web platform from which to launch their ministry.

We're looking for a highly creative web developer that can grasp the vision for this site and take ownership of the development to conceive engaging additional details and elements for the site.

A cookie cutter website template just won't do it for this one. Even though the initial site is not large, it should feel highly designed and highly engaging. In the words of their Senior Pastor: “We want people to realize that if we care this much about a website, imagine how much more we're going care about their family!”

Details: HopeHaven - Temecula is a new church plant in Temecula, CA built on a self-replicating "missionary" model. Essentially, the goal is to attract people, point them to Christ, develop them into mature Christians and send them out to plant churches as part of church plant "teams". This model resembles more of what is done overseas then in the USA.

As well, the Church is what is called "Family Integrated" which means that it ministers to the family as well as the individual. That means children and parents attend services together as a family unit. As such, the site needs to be "family friendly" and welcoming.

The Logo files are attached. They do not need to drive the palette of the site per se but the logo should look like it "belongs" on the site.

Website has 6 main landing pages with limited add'l content pages.

No Flash. Should look good on mobile as well as traditional browser.

Should be "scalable" - easy to expand nav bars, pages, etc as the church grows with ability to add plug ins (like Google maps or iTunes podcast downloads).

PLEASE SEE ATTACHED DOCUMENT: HH-T Website Info.doc for more details.

Logo File attached below.

Use your imagination! Have fun... design a church website that you would want to visit and interact with. If you think of things we might have missed that add great functionality, value, uniqueness or enhance user experience, add them!!! God bless!

Another Marlowe Studios Inc/Pixel Forum Job. Thanks again Designers!

• Must be a fully coded, functional website.

Site must be tested and good to go in IE 7+, Firefox 9+, Chrome and both Apple and Android Mobile platforms.

Blog must be one that church can easily upload content to as an integrated part of the site (no Postwright.example, etc plugins please).

Final handover must include full rights to the designs, stock art, coding, etc (so, no "one use templates" please).

Must be a user-scalable platform on a user friendly CMS (CMS is designers choice so long as it is industry standard and user friendly). We want the church to be able to add or modify page elements themselves.

Final handover will include loading and testing on to our hosting server.

The designer must be willing to support the site for 30 days after launch as part of the site payment.
• Prefer a custom designed template (should not look like a "cookie cutter" site).

See attached doc for more!
• Any non-standard CMS or industry unsupported plugins.

No Flash.

```html
<!DOCTYPE html>
<html lang="en">
<head>
<meta charset="utf-8">
<title>HopeHaven</title>
<link rel="stylesheet" href="https://fonts.googleapis.com/css2?family=Open+Sans:ital,wght@0,300;0,400;0,600;1,400&family=Roboto+Slab:wght@400&display=swap">
<style>
:root{
  --page:#f1f2ec;
  --panel:#f9faf5;
  --band:#ebede3;
  --ink:#3a3a36;
  --muted:#8c8c84;
  --olive:#8a8a1c;
  --accent:#b4472f;
  --dark:#3b3a37;
  --rule:#2b2b2b;
}
*{box-sizing:border-box;margin:0;padding:0}
html,body{width:1200px;height:971px;overflow:hidden}
body{position:relative;background:var(--page);font-family:"Open Sans",Arial,sans-serif;color:var(--ink)}
.abs{position:absolute}
.top-rule{left:0;top:3px;width:1200px;height:2px;background:var(--rule)}

/* header */
.brand{left:438px;top:16px;width:202px;height:62px;display:flex;align-items:center;gap:8px}
.brand-mark{width:22px;height:22px;border-radius:50%;background:var(--accent);flex:none}
.brand-name{font-size:22px;font-weight:600;color:var(--ink);line-height:1}
.next-event{right:284px;top:19px;text-align:right}
.next-event .lead{font-size:8px;color:#333}
.next-event .title{font-size:13px;color:var(--olive);margin-top:5px}
.next-event .countdown{font-size:9.5px;color:#222;margin-top:6px}

.nav-band{left:0;top:87px;width:1200px;height:22px;background:var(--band)}
.main-nav a{position:absolute;top:93px;font-size:7.5px;color:var(--olive);text-decoration:none;text-transform:uppercase;letter-spacing:.3px}

/* hero */
.hero{left:0;top:109px;width:1200px;height:266px;background:radial-gradient(ellipse at 55% 40%,#7c4a3c 0%,#55302a 40%,#1d100d 78%,#080504 100%)}
.hero-title{left:297px;top:160px;font-size:20px;font-weight:300;color:#fff}
.hero-copy{left:297px;top:196px;width:292px;font-size:8.5px;line-height:10.5px;font-weight:300;color:#eee}
.hero-label{left:297px;top:240px;font-size:8.5px;color:#eee;font-weight:300}
.hero-input{left:297px;top:255px;width:154px;height:20px;border:1px solid #c9b4ab;background:transparent}
.hero-send{left:297px;top:287px;width:32px;height:17px;background:var(--accent);color:#fff;font-size:8px;display:flex;align-items:center;justify-content:center}
.hero-book{left:628px;top:135px;width:285px;height:195px;background:linear-gradient(160deg,#c25a45,#9a3c2c);transform:skewY(8deg);border-radius:3px;opacity:.95}

/* panel */
.panel{left:297px;top:367px;width:619px;height:481px;background:var(--panel);box-shadow:0 3px 6px rgba(0,0,0,.35)}
.h2{font-size:13px;font-weight:400;color:#2f2f2c}
.link{font-size:7.5px;font-weight:400;color:var(--accent)}
.small{font-size:7px;line-height:10.5px;font-weight:400;color:#555}
.meta{font-size:6px;font-style:italic;font-weight:400;color:var(--muted)}

.sermon-img{width:130px;height:94px;display:flex;align-items:center;justify-content:center;font-family:"Roboto Slab",Georgia,serif;font-size:24px;color:#fff;text-shadow:0 1px 3px rgba(0,0,0,.4)}
.sky-values{background:linear-gradient(180deg,#5f8f9a,#a7c5c4 55%,#3d6670)}
.sky-hope{background:linear-gradient(180deg,#2c3f5c,#54709a 50%,#b8c8d8)}
.sky-believe{background:linear-gradient(180deg,#d28a8a,#7c3a4e 55%,#3a2035)}
.sermon-title{font-size:8.5px;color:var(--accent)}
.icons{display:flex;gap:4px}
.icon{width:17px;height:15px;background:var(--accent);display:flex;align-items:center;justify-content:center}

.event-title{font-size:8.5px;color:var(--accent)}
.datebox{width:22px;flex:none}
.datebox .mon{height:13px;background:var(--olive);color:#fff;font-size:6px;text-align:center;line-height:13px}
.datebox .day{height:22px;background:var(--dark);color:#fff;font-size:12px;text-align:center;line-height:22px}

.news-title{font-size:8.5px;color:var(--accent)}
.news-meta{font-size:5.5px;font-style:italic;color:#555}
.news-meta em{color:var(--accent)}
.news-photo{width:77px;height:57px;flex:none;background:linear-gradient(180deg,#6f8a70,#3a4a3e 60%,#1f2a22)}

/* footer */
.foot-brand{left:560px;top:867px;width:104px;height:28px;display:flex;align-items:center;gap:5px}
.foot-brand .brand-mark{width:11px;height:11px;background:#666}
.foot-brand span{font-size:11px;font-weight:600;color:#4a4a46}
.foot-nav a{position:absolute;top:912px;font-size:6.5px;color:var(--olive);text-decoration:none;text-transform:uppercase}
.copyright{left:526px;top:932px;font-size:6px;color:#555}
.copyright b{color:var(--olive);font-weight:600}
.social{left:550px;top:950px;display:flex;gap:7px}
.social i{width:10px;height:10px;border-radius:50%;background:#9a9a96;display:block}
</style>
</head>
<body>
<div class="abs top-rule"></div>

<header>
  <div class="abs brand">
    <span class="brand-mark"></span>
    <div class="brand-name">HopeHaven</div>
  </div>
  <div class="abs next-event">
    <p class="lead">Join us at our next event</p>
    <p class="title">Mission Trip Meeting</p>
    <p class="countdown">9 days 11 hours 33 minutes 7 seconds</p>
  </div>
</header>

<div class="abs nav-band"></div>
<nav class="main-nav">
  <a style="left:297px">Home</a><a style="left:387px">We Are</a><a style="left:511px">Give</a>
  <a style="left:636px">Blog</a><a style="left:763px">Know Jesus?</a><a style="left:916px">Reach Us</a>
</nav>

<section class="abs hero" role="img" aria-label="Curved wooden plank wall in warm brown tones"></section>
<div class="abs hero-book" role="img" aria-label="Red booklet titled Live Life to the Fullest"></div>
<h1 class="abs hero-title">Attention Grabbing.</h1>
<p class="abs hero-copy">For this example we have an image, title, text content, a button and also a newsletter sign-up form all within the slider – super simple setup and attention grabbing with your visitors.</p>
<p class="abs hero-label">Your Email (required)</p>
<div class="abs hero-input"></div>
<div class="abs hero-send">Send</div>

<main class="abs panel">
  <h2 class="abs h2" style="left:10px;top:14px">Latest Sermons</h2>
  <p class="abs small" style="left:10px;top:36px;width:118px">Et zzril dolore augue consectetuer amet. Suscipit tincidunt ii velit nibh lorem. Modo per notare ii claritatem facer.</p>
  <a class="abs link" style="left:10px;top:93px">View all sermons</a>

  <div class="abs" style="left:154px;top:16px">
    <div class="sermon-img sky-values" role="img" aria-label="Cloudy teal sky">VALUES</div>
    <p class="sermon-title" style="margin-top:12px">Sermon 3</p>
    <div class="icons" style="margin-top:6px">
      <span class="icon"><svg width="7" height="7" viewBox="0 0 7 7"><path d="M0 2h2l2-2v7L2 5H0z" fill="#fff"/></svg></span>
      <span class="icon"><svg width="8" height="6" viewBox="0 0 8 6"><rect width="5" height="6" fill="#fff"/><path d="M5 3l3-2v4z" fill="#fff"/></svg></span>
      <span class="icon"><svg width="6" height="7" viewBox="0 0 6 7"><rect width="6" height="7" fill="#fff"/><path d="M1 3h4M1 5h4" stroke="#b4472f"/></svg></span>
    </div>
    <p class="meta" style="margin-top:7px">◷ September 12th, 2012</p>
    <p class="meta" style="margin-top:2px">● admin</p>
  </div>
  <div class="abs" style="left:309px;top:16px">
    <div class="sermon-img sky-hope" role="img" aria-label="Blue sky with clouds">HOPE</div>
    <p class="sermon-title" style="margin-top:12px">Sermon 2</p>
    <div class="icons" style="margin-top:6px">
      <span class="icon"><svg width="7" height="7" viewBox="0 0 7 7"><path d="M0 2h2l2-2v7L2 5H0z" fill="#fff"/></svg></span>
      <span class="icon"><svg width="8" height="6" viewBox="0 0 8 6"><rect width="5" height="6" fill="#fff"/><path d="M5 3l3-2v4z" fill="#fff"/></svg></span>
    </div>
    <p class="meta" style="margin-top:7px">◷ September 12th, 2012</p>
    <p class="meta" style="margin-top:2px">● admin</p>
  </div>
  <div class="abs" style="left:465px;top:16px">
    <div class="sermon-img sky-believe" role="img" aria-label="Pink and purple sunset clouds">BELIEVE</div>
    <p class="sermon-title" style="margin-top:12px">Sermon 1</p>
    <div class="icons" style="margin-top:6px">
      <span class="icon"><svg width="6" height="7" viewBox="0 0 6 7"><rect width="6" height="7" fill="#fff"/><path d="M1 3h4M1 5h4" stroke="#b4472f"/></svg></span>
    </div>
    <p class="meta" style="margin-top:7px">◷ September 12th, 2012</p>
    <p class="meta" style="margin-top:2px">● admin</p>
  </div>

  <h2 class="abs h2" style="left:10px;top:193px">Upcoming Events</h2>

  <article class="abs" style="left:10px;top:222px;width:130px">
    <p class="event-title">Mission Trip Meeting</p>
    <div style="display:flex;gap:9px;margin-top:9px">
      <div class="datebox"><div class="mon">SEP</div><div class="day">30</div></div>
      <p class="small" style="width:99px">Quisque facilisis erat a dui. Nam malesuada ornare dolor. Cras gravida, diam sit amet rhoncus</p>
    </div>
    <p class="meta" style="margin-top:14px">◷ 6:00pm to 9:00pm</p>
    <p class="meta" style="margin-top:3px">⚲ Our Church</p>
  </article>
  <article class="abs" style="left:154px;top:222px;width:130px">
    <p class="event-title">Feeding the World</p>
    <div style="display:flex;gap:9px;margin-top:9px">
      <div class="datebox"><div class="mon">DEC</div><div class="day">09</div></div>
      <p class="small" style="width:99px">Quisque facilisis erat a dui. Nam malesuada ornare dolor. Cras gravida, diam sit amet rhoncus</p>
    </div>
    <p class="meta" style="margin-top:14px">◷ 7:00pm - 9:00pm</p>
    <p class="meta" style="margin-top:3px">⚲ Pastor Dan's House</p>
  </article>
  <article class="abs" style="left:10px;top:334px;width:130px">
    <p class="event-title">Single Parent Support</p>
    <div style="display:flex;gap:9px;margin-top:9px">
      <div class="datebox"><div class="mon">OCT</div><div class="day">03</div></div>
      <p class="small" style="width:99px">Quisque facilisis erat a dui. Nam malesuada ornare dolor. Cras gravida, diam sit amet rhoncus</p>
    </div>
    <p class="meta" style="margin-top:14px">◷ 11:00am - 3:00am</p>
    <p class="meta" style="margin-top:3px">⚲ Youth Group Auditorium</p>
  </article>
  <article class="abs" style="left:154px;top:334px;width:130px">
    <p class="event-title">Handling the Holidays</p>
    <div style="display:flex;gap:9px;margin-top:9px">
      <div class="datebox"><div class="mon">NOV</div><div class="day">29</div></div>
      <p class="small" style="width:99px">Quisque facilisis erat a dui. Nam malesuada ornare dolor. Cras gravida, diam sit amet rhoncus</p>
    </div>
    <p class="meta" style="margin-top:14px">◷ 9am - 12:00pm</p>
    <p class="meta" style="margin-top:3px">⚲ Main Auditorium</p>
  </article>
  <a class="abs link" style="left:10px;top:440px">View all events</a>

  <h2 class="abs h2" style="left:310px;top:193px">Latest News</h2>
  <article class="abs" style="left:310px;top:222px;width:285px">
    <p class="news-title">Gallery Post Format</p>
    <p class="news-meta" style="margin-top:2px">August 7th, 2012 &nbsp;Posted by: admin &nbsp;Posted in: <em>Gallery Format</em></p>
    <p class="small" style="margin-top:6px">Example of a Post Type of Gallery in PressKit – this will automatically gather any attached images to a post</p>
  </article>
  <article class="abs" style="left:310px;top:290px;width:285px">
    <p class="news-title">Tweet Embed Post</p>
    <p class="news-meta" style="margin-top:2px">August 2nd, 2012 &nbsp;Posted by: admin &nbsp;Posted in: <em>Status</em></p>
    <p class="small" style="margin-top:6px">I am seldom happy with the way fonts display in the browser in comparison to how they display in ImageLab</p>
  </article>
  <article class="abs" style="left:310px;top:361px;width:285px;display:flex;gap:10px">
    <div class="news-photo" role="img" aria-label="Waterfall in a green landscape"></div>
    <div style="width:198px">
      <p class="news-title">Standard Post Format</p>
      <p class="news-meta" style="margin-top:2px">August 2nd, 2012 &nbsp;Posted by: admin &nbsp;Posted in: <em>Standard</em></p>
      <p class="small" style="margin-top:6px">Welcome to the good of standard post format – you can add a featured image or not, type your post</p>
    </div>
  </article>
  <a class="abs link" style="left:310px;top:439px">View all news</a>
</main>

<footer>
  <div class="abs foot-brand"><span class="brand-mark"></span><span>HopeHaven</span></div>
  <nav class="foot-nav">
    <a style="left:494px">Home</a><a style="left:524px">We Are</a><a style="left:564px">Give</a>
    <a style="left:599px">Blog</a><a style="left:630px">Know Jesus?</a><a style="left:692px">Reach Us</a>
  </nav>
  <p class="abs copyright">©2012 &nbsp; <b>HopeHaven</b></p>
  <div class="abs social" aria-label="Social links"><i></i><i></i><i></i><i></i><i></i><i></i><i></i></div>
</footer>
</body>
</html>
```